The most modern business card ever !!!

Our company call “Vantilo”. Vantilo is a technology company specialized in cruises solutions. Out main product is a platform to reserve cruises. This is a revolutionary platform that make easier to travel agencies and final users to reserve cruises across dozen companies like tarvik, welbi, dpv, hbt, etc..We are a “start up”, with a young team of developers and we want to transmit it.. For it, we want something different, a modern business card that represent cruises and technology.. When someone receive this card, this person should say: wowww this is different… this is modern… this is a cruise related company..
Contact Information for Business Card
Requirements
Must have
- diferent, modern
Should not have
- traditions business card

```html
<!DOCTYPE html>
<html lang="en">
<head>
<meta charset="utf-8">
<title>Vantilo — Business Card</title>
<link rel="stylesheet" href="https://fonts.googleapis.com/css2?family=Exo+2:wght@400;600;700&display=swap">
<style>
  :root {
    --page-bg: #161617;
    --card-top: #2e2e30;
    --card-bottom: #19191a;
    --text-main: #f2f2f2;
    --accent: #2aa8e0;
    --cut-dark: #0d0d0e;
    --cut-mid: #1f1f21;
  }
  * { margin: 0; padding: 0; box-sizing: border-box; }
  html, body {
    width: 1200px; height: 774px; overflow: hidden;
    background: var(--page-bg);
    font-family: "Exo 2", sans-serif;
    color: var(--text-main);
  }
  .stage { position: relative; width: 1200px; height: 774px; }
  .card {
    position: absolute;
    width: 540px; height: 310px;
    border-radius: 16px;
    background: linear-gradient(160deg, var(--card-top) 0%, var(--card-bottom) 100%);
    box-shadow: 0 10px 30px rgba(0,0,0,0.5);
    overflow: hidden;
  }
  .card-front { left: 40px; top: 232px; }
  .card-back  { left: 620px; top: 232px; }

  .brand-name {
    font-weight: 600;
    letter-spacing: 2px;
    color: var(--text-main);
    line-height: 1;
  }
  .card-front .brand-name { position: absolute; left: 38px; top: 30px; font-size: 50px; }
  .card-back .brand-name { position: absolute; right: 60px; top: 128px; font-size: 56px; }

  .contact-list {
    position: absolute; left: 34px; top: 104px;
    list-style: none;
    display: flex; flex-direction: column; gap: 12px;
  }
  .contact-item { display: flex; align-items: center; gap: 12px; }
  .contact-icon {
    width: 28px; height: 28px; flex: none;
    border-radius: 50%;
    background: var(--accent);
    display: flex; align-items: center; justify-content: center;
  }
  .contact-icon svg { width: 16px; height: 16px; }
  .contact-text { font-size: 12.5px; line-height: 1.35; letter-spacing: 0.6px; }
  .person-name { font-weight: 700; font-size: 14px; letter-spacing: 1.4px; text-transform: uppercase; }
  .person-role { color: var(--accent); font-size: 11.5px; text-transform: uppercase; letter-spacing: 1px; }
  .label { color: var(--accent); margin-right: 4px; }

  .cut-pattern {
    position: absolute;
    background: linear-gradient(135deg, var(--cut-mid) 0%, var(--cut-dark) 100%);
  }
  .card-front .cut-pattern {
    right: 34px; top: 60px; width: 200px; height: 220px;
    clip-path: polygon(0 0, 100% 0, 100% 100%, 0 100%, 0 82%, 55% 82%, 55% 18%, 0 18%);
  }
  .card-back .cut-pattern {
    left: 30px; top: 22px; width: 220px; height: 266px;
    clip-path: polygon(0 0, 100% 0, 100% 22%, 35% 22%, 35% 100%, 0 100%);
  }
</style>
</head>
<body>
<main class="stage">

  <section class="card card-front">
    <div class="brand-name">Vantilo</div>

    <ul class="contact-list">
      <li class="contact-item">
        <span class="contact-icon">
          <svg viewBox="0 0 16 16"><circle cx="8" cy="5.5" r="3" fill="#fff"/><path d="M2.5 14c0-3 2.5-5 5.5-5s5.5 2 5.5 5z" fill="#fff"/></svg>
        </span>
        <div class="contact-text">
          <div class="person-name">Marcus Delane</div>
          <div class="person-role">CEO/Founder</div>
        </div>
      </li>
      <li class="contact-item">
        <span class="contact-icon">
          <svg viewBox="0 0 16 16"><path d="M4 1.5l2.4 3-1.3 1.6c.8 1.8 2.1 3.1 3.9 3.9l1.6-1.3 3 2.4-1.5 2.4C7 13.2 2.8 9 2.5 3z" fill="#fff"/></svg>
        </span>
        <div class="contact-text">
          <div><span class="label">P:</span>+1 555-214-0187</div>
          <div><span class="label">F:</span>+1 555-214-0187</div>
        </div>
      </li>
      <li class="contact-item">
        <span class="contact-icon">
          <svg viewBox="0 0 16 16" fill="none" stroke="#fff" stroke-width="1.3"><circle cx="8" cy="8" r="6"/><ellipse cx="8" cy="8" rx="2.6" ry="6"/><line x1="2" y1="8" x2="14" y2="8"/></svg>
        </span>
        <div class="contact-text">
          <div><span class="label">E:</span>marcus@vantilo.com</div>
          <div><span class="label">W:</span>www.vantilo.com</div>
        </div>
      </li>
      <li class="contact-item">
        <span class="contact-icon">
          <svg viewBox="0 0 16 16"><path d="M8 1a4.5 4.5 0 0 0-4.5 4.5C3.5 9 8 15 8 15s4.5-6 4.5-9.5A4.5 4.5 0 0 0 8 1z" fill="#fff"/><circle cx="8" cy="5.5" r="1.7" fill="#2aa8e0"/></svg>
        </span>
        <div class="contact-text">
          <div>1840 Harbor Way</div>
          <div>Seabright, CA 90000, USA</div>
        </div>
      </li>
    </ul>

    <div class="cut-pattern" role="img" aria-label="Die-cut pattern of small square holes"></div>
  </section>

  <section class="card card-back">
    <div class="cut-pattern" role="img" aria-label="Die-cut pattern of small square holes"></div>
    <div class="brand-name">Vantilo</div>
  </section>

</main>
</body>
</html>
```